R&D and Engineering Management Consultancy Needs Branding

I need a branding style for my consultancy - specifically I need business cards by Tuesday 26 April (9 days away!) to take to a conference, including a logo design. If this service does not include printing I will need it in time for printing.

Later, the same logo and style needs to be incorporated into a Powerpoint template and a Word Template. Optionally also a Pages template.

The branding image needs to project and/or support the following qualities:
High tech
Speed and throughput
Lean
Innovation
Dependability
Quality

One possible concept is based on the Principal’s surname – Marrowby, which is a small bird. So a logo design which is a stylized rendition of a bird may work well. Flight implies speed, and the style would be “techy”, perhaps geometric in a way that conveys Lean – boiling things down to the essential elements.

Other concepts are welcome.
You can find me on https://au.peoplenexa.com/in/hollismarrowby

Business Card Information
Marrowby Consulting
Hollis Marrowby
BE (Hons), CSM, CSPO, SA
Principal Consultant
Mobile: +61 (0)455 913 607
Email: hollis@marrowbyconsulting.com
Web: www.marrowbyconsulting.com

Reverse:
Lean/Agile Software Development at Scale
Lean Product Development
Lean Portfolio Management
Organisational development and transformation
Mentoring and coaching of Technical Leaders
Program and project management
Business Processes and Systems

Target Market(s)

The target market for this consultancy comprises technology-based product and/or services development companies. They typically engage in one or a mix of software, electronics, mechanical, ASIC and MEMS development activities. They range from small startups to transnational corporations staffed by highly skilled engineers, developers and scientists. The consultancy is applicable across a range of domains such as biomedical device development, inkjet printing technology, telecommunications, internet and mesh networking technologies, renewable energy systems, and electronic product development of all kinds.

Industry/Entity Type

Information Technology

Contact Information for Business Card

Marrowby Consulting
Hollis Marrowby
BE (Hons), CSM, CSPO, SA
Principal Consulting

Reverse:
➢ Lean/Agile Software Development
➢ Lean Product Development
➢ Lean Portfolio Management
➢ Organisational development and transformation
➢ Mentoring and coaching of Technical Leaders
➢ Program and project management
➢ Business Processes and Systems

Logo Text

Just graphical

Font styles to use
Sans Serif

Requirements
Must have
• A clean professional look
Nice to have
• Use a bird motif based on my name Marrowby
• The bird's colours are yellow/gold, light brown, black and red so these suggest a colour scheme.
• I have uploaded a stylised bird design that I like but this belongs to another company. A variation on this might be good.
Should not have
• Too much clutter. If the details are too much to fit, drop the qualifications line

```html
<!DOCTYPE html>
<html lang="en">
<head>
<meta charset="utf-8">
<title>Marrowby Consulting – Business Card</title>
<link rel="stylesheet" href="https://fonts.googleapis.com/css2?family=Source+Sans+3:wght@400;600;700&display=swap">
<style>
  :root {
    --teal-deep: #034a49;
    --signal-yellow: #fdfd38;
    --paper-white: #ffffff;
    --divider: #8fb3ad;
    --ink-dark: #0b4a45;
  }
  html, body {
    margin: 0;
    padding: 0;
    width: 1200px;
    height: 686px;
    overflow: hidden;
    background: var(--teal-deep);
  }
  .card {
    position: relative;
    width: 1200px;
    height: 686px;
    background: var(--teal-deep);
    font-family: "Source Sans 3", "Myriad Pro", Arial, sans-serif;
    color: var(--paper-white);
    overflow: hidden;
  }
  .brand-mark {
    position: absolute;
    left: 150px;
    top: 158px;
    width: 260px;
    height: 260px;
  }
  .brand-name {
    position: absolute;
    left: 37px;
    top: 470px;
    width: 546px;
    margin: 0;
    font-size: 55px;
    font-weight: 600;
    line-height: 1;
    color: var(--signal-yellow);
    white-space: nowrap;
  }
  .divider {
    position: absolute;
    left: 623px;
    top: 66px;
    width: 1px;
    height: 548px;
    background: var(--divider);
  }
  .person {
    position: absolute;
    left: 711px;
    top: 176px;
  }
  .person-name {
    margin: 0 0 14px;
    font-size: 41px;
    font-weight: 700;
    line-height: 1.1;
    color: var(--signal-yellow);
  }
  .person-line {
    margin: 0;
    font-size: 31px;
    font-weight: 400;
    line-height: 54px;
  }
  .contact {
    position: absolute;
    left: 705px;
    top: 440px;
    margin: 0;
    padding: 0;
    list-style: none;
    font-size: 25px;
    line-height: 47px;
  }
  .contact-item::before {
    content: ":";
    display: inline-block;
    width: 21px;
  }
  .footer-band {
    position: absolute;
    left: 0;
    top: 614px;
    width: 1200px;
    height: 72px;
    background: var(--signal-yellow);
    display: flex;
    align-items: center;
    justify-content: center;
  }
  .web-address {
    font-size: 22px;
    font-weight: 400;
    color: var(--ink-dark);
    letter-spacing: 0.2px;
  }
</style>
</head>
<body>
  <main class="card">
    <svg class="brand-mark" viewBox="0 0 260 260" aria-hidden="true">
      <circle cx="130" cy="130" r="125" fill="none" stroke="var(--signal-yellow)" stroke-width="4"/>
    </svg>
    <h1 class="brand-name">Marrowby Consulting</h1>

    <div class="divider"></div>

    <section class="person">
      <h2 class="person-name">Hollis Marrowby</h2>
      <p class="person-line">BE (Hons), CSM, CSPO, SA</p>
      <p class="person-line">Principal Consulting</p>
    </section>

    <ul class="contact">
      <li class="contact-item">+61 (0)455 913 607</li>
      <li class="contact-item">hollis@marrowbyconsulting.com</li>
    </ul>

    <footer class="footer-band">
      <span class="web-address">www.marrowbyconsulting.com</span>
    </footer>
  </main>
</body>
</html>
```